New Office Poster Designs

Attached you will find 3 poster designs that we found online along with our logos. Please use our logos to reference any type of color or design.
These posters will be hung around our Loan Offices.

INSTRUCTIONS: Please mimic all 3 posters (MINUS THE SMALL WRITING ON THEM THAT IS NOT IN ENGLISH IGNORE THAT)
but use our logos and colors. Also, if you can make them in Spanish as well as English that is a plus. We will also need 1 additional poster with the below wording.

Additional Poster:
Stuck in a Title Loan? Let us pay it off up to $10,000

Target Market(s)

People looking to get a loan and need money

Industry/Entity Type

Loan Industry - Consumer Lending - Fast easy loans

Requirements
Nice to have
• English and Spanish

```html
<!DOCTYPE html>
<html lang="es">
<head>
<meta charset="utf-8">
<title>Vela Credit – Office Posters</title>
<link href="https://fonts.googleapis.com/css2?family=Poppins:ital,wght@0,400;0,500;0,600;0,700;0,800;1,400;1,500;1,600&display=swap" rel="stylesheet">
<style>
  :root{
    --red:#c1272d;
    --red-dark:#9e1d22;
    --green:#1f6b3a;
    --green-dark:#154d29;
    --white:#ffffff;
    --ink:#1b1b1b;
    --pill:#e9e9e9;
    --stage-top:#ececec;
    --stage-bottom:#d5d5d5;
  }
  *{box-sizing:border-box;margin:0;padding:0}
  html,body{width:1200px;height:2400px;overflow:hidden}
  body{font-family:"Poppins",sans-serif;background:var(--stage-bottom);position:relative}
  .stage-top{position:absolute;left:0;top:0;width:1200px;height:1146px;background:var(--stage-top)}

  .poster{position:absolute;overflow:hidden;box-shadow:0 6px 14px rgba(0,0,0,.25)}
  .poster.tall{width:415px;height:590px}
  .poster.block{width:425px;height:550px}
  .poster.featured{left:272px;top:92px;transform:scale(1.66);transform-origin:top left}
  .poster.p-approval{left:173px;top:1191px}
  .poster.p-amount{left:612px;top:1191px}
  .poster.p-title{left:163px;top:1799px}
  .poster.p-credit{left:612px;top:1799px}

  .bg{position:absolute;left:0;width:100%}
  .bg-red{background:radial-gradient(circle at 30% 40%,#cc3338,var(--red) 60%,var(--red-dark))}
  .bg-green{background:radial-gradient(circle at 60% 50%,#2a7a47,var(--green) 60%,var(--green-dark))}
  .frame{position:absolute;inset:12px;border:1.5px solid rgba(255,255,255,.9);pointer-events:none}

  /* tall posters */
  .tall .bg-red{top:0;height:215px}
  .tall .bg-green{top:215px;height:375px}
  .logo-tab{position:absolute;left:123px;top:0;width:169px;height:78px;background:var(--white);
    clip-path:polygon(0 0,100% 0,88% 100%,12% 100%);text-align:center;padding-top:22px}
  .brand-name{font-weight:600;color:var(--green);font-size:20px;line-height:1}
  .brand-url{font-size:6.5px;color:var(--green);margin-top:4px}
  .headline{position:absolute;left:0;width:100%;text-align:center;color:var(--white)}
  .headline .big{font-weight:800;font-size:37px;line-height:1.12;letter-spacing:.5px}
  .headline .kicker{font-weight:800;font-size:27px;line-height:1.1}
  .headline .amount{font-weight:800;font-size:52px;line-height:1}
  .headline .sub{font-style:italic;font-weight:500;font-size:17px;margin-top:4px}
  .mark{position:absolute;left:0;top:232px;width:100%;height:150px;display:flex;align-items:center;justify-content:center;
    color:var(--white);font-weight:600;font-size:46px}
  .info{position:absolute;left:14px;right:14px;top:386px;bottom:18px;background:var(--white)}
  .info .row{position:absolute;left:34px;right:34px;top:14px;display:flex;align-items:center;justify-content:space-between}
  .offer strong{display:block;color:var(--green);font-weight:700;font-size:16px;line-height:1.1}
  .offer em{display:block;color:var(--green);font-size:14px;line-height:1.2}
  .phone{background:var(--pill);border-radius:16px;color:var(--red);font-weight:700;font-size:21px;padding:2px 12px;letter-spacing:.5px}
  .rule{position:absolute;left:34px;right:34px;top:66px;border-top:1.2px solid #bbb}
  .copy{position:absolute;left:34px;right:34px;top:76px;color:var(--ink)}
  .copy p{font-size:6.3px;line-height:1.35;margin-bottom:8px}
  .copy .lead{font-weight:600}
  .copy .note{font-style:italic}
  .url-tab{position:absolute;left:96px;width:223px;top:546px;height:30px;background:var(--green-dark);
    border-radius:12px 12px 0 0;color:var(--white);font-weight:700;font-size:14px;text-align:center;line-height:30px}
  .tall .base{position:absolute;left:0;right:0;bottom:0;height:14px;background:var(--green-dark)}

  /* square-logo posters */
  .block .bg-green{top:0;height:424px}
  .block .bg-red{top:424px;height:126px}
  .panel{position:absolute;left:24px;top:210px;width:377px;height:307px;background:var(--white)}
  .panel .brand-name{position:absolute;left:0;right:0;top:94px;text-align:center;font-size:46px}
  .panel .bar{position:absolute;left:12px;right:12px;bottom:26px;height:37px;background:var(--green);
    color:var(--white);font-weight:700;font-size:17px;text-align:center;line-height:37px}
  .title-head{position:absolute;left:0;width:100%;top:44px;text-align:center;color:var(--white)}
  .title-head .q{font-weight:500;font-size:10.5px}
  .title-head .kicker{font-weight:800;font-size:27px;line-height:1.25;margin-top:4px}
  .title-head .amount{font-weight:800;font-size:56px;line-height:1}
  .title-head .sub{font-style:italic;font-size:11.5px;margin-top:12px}
  .no-box{position:absolute;left:27px;top:26px;width:188px;height:106px;background:var(--white);
    color:var(--green);font-weight:800;font-size:84px;line-height:106px;text-align:center;letter-spacing:-2px}
  .credit{position:absolute;left:234px;top:38px;color:var(--white);font-weight:800;font-size:40px;line-height:1.12}
  .credit-note{position:absolute;left:45px;right:45px;top:140px;color:var(--white);font-size:11.5px;line-height:1.35;text-align:center}
</style>
</head>
<body>
  <div class="stage-top"></div>

  <!-- Featured: instant approval -->
  <article class="poster tall featured">
    <div class="bg bg-red" role="img" aria-label="Red banknote engraving pattern"></div>
    <div class="bg bg-green" role="img" aria-label="Green banknote engraving with eagle emblem"></div>
    <div class="frame"></div>
    <div class="logo-tab"><div class="brand-name">Vela Credit</div><div class="brand-url">www.VelaCredit.com</div></div>
    <div class="headline" style="top:88px"><div class="big">INSTANTE<br>APROBACIÓN</div><div class="sub">( INSTANT APPROVAL )</div></div>
    <div class="mark">Vela Credit</div>
    <div class="base"></div>
    <div class="info">
      <div class="row"><div class="offer"><strong>Tiempo limitado</strong><em>(Limited time)</em></div><div class="phone">0123-456-789</div></div>
      <div class="rule"></div>
      <div class="copy">
        <p class="lead">Lorem ipsum dolor sit amet, consectetur adipiscing elit, sed do eiusmod tempor incididunt ut labore et dolore magna aliqua. Ut enim ad minim veniam, quis nostrud exercitation ullamco laboris nisi ut aliquip ex ea commodo consequat. Duis aute irure dolor in reprehenderit in voluptate velit esse cillum dolore eu fugiat nulla pariatur.</p>
        <p class="note">Lorem ipsum dolor sit amet, consectetur adipiscing elit, sed do eiusmod tempor incididunt ut labore et dolore magna aliqua. Ut enim ad minim veniam, quis nostrud exercitation ullamco laboris nisi ut aliquip ex ea commodo consequat. Duis aute irure dolor in reprehenderit in voluptate velit esse cillum dolore eu fugiat nulla pariatur.</p>
      </div>
    </div>
    <div class="url-tab">www.velacredit.com</div>
  </article>

  <!-- Instant approval -->
  <article class="poster tall p-approval">
    <div class="bg bg-red" role="img" aria-label="Red banknote engraving pattern"></div>
    <div class="bg bg-green" role="img" aria-label="Green banknote engraving with eagle emblem"></div>
    <div class="frame"></div>
    <div class="logo-tab"><div class="brand-name">Vela Credit</div><div class="brand-url">www.VelaCredit.com</div></div>
    <div class="headline" style="top:88px"><div class="big">INSTANTE<br>APROBACIÓN</div><div class="sub">( INSTANT APPROVAL )</div></div>
    <div class="mark">Vela Credit</div>
    <div class="base"></div>
    <div class="info">
      <div class="row"><div class="offer"><strong>Tiempo limitado</strong><em>(Limited time)</em></div><div class="phone">0123-456-789</div></div>
      <div class="rule"></div>
      <div class="copy">
        <p class="lead">Lorem ipsum dolor sit amet, consectetur adipiscing elit, sed do eiusmod tempor incididunt ut labore et dolore magna aliqua. Ut enim ad minim veniam, quis nostrud exercitation ullamco laboris nisi ut aliquip ex ea commodo consequat. Duis aute irure dolor in reprehenderit in voluptate velit esse cillum dolore eu fugiat nulla pariatur.</p>
        <p class="note">Lorem ipsum dolor sit amet, consectetur adipiscing elit, sed do eiusmod tempor incididunt ut labore et dolore magna aliqua. Ut enim ad minim veniam, quis nostrud exercitation ullamco laboris nisi ut aliquip ex ea commodo consequat. Duis aute irure dolor in reprehenderit in voluptate velit esse cillum dolore eu fugiat nulla pariatur.</p>
      </div>
    </div>
    <div class="url-tab">www.velacredit.com</div>
  </article>

  <!-- Get up to $10,000 -->
  <article class="poster tall p-amount">
    <div class="bg bg-red" role="img" aria-label="Red banknote engraving pattern"></div>
    <div class="bg bg-green" role="img" aria-label="Green-tinted photo of scattered dollar bills"></div>
    <div class="frame"></div>
    <div class="logo-tab"><div class="brand-name">Vela Credit</div><div class="brand-url">www.VelaCredit.com</div></div>
    <div class="headline" style="top:92px"><div class="kicker">OBTENGA HASTA</div><div class="amount">$10,000</div><div class="sub">( GET UP TO $10,000 )</div></div>
    <div class="mark">Vela Credit</div>
    <div class="base"></div>
    <div class="info">
      <div class="row"><div class="offer"><strong>Tiempo limitado</strong><em>(Limited time)</em></div><div class="phone">0123-456-789</div></div>
      <div class="rule"></div>
      <div class="copy">
        <p class="lead">Lorem ipsum dolor sit amet, consectetur adipiscing elit, sed do eiusmod tempor incididunt ut labore et dolore magna aliqua. Ut enim ad minim veniam, quis nostrud exercitation ullamco laboris nisi ut aliquip ex ea commodo consequat. Duis aute irure dolor in reprehenderit in voluptate velit esse cillum dolore eu fugiat nulla pariatur.</p>
        <p class="note">Lorem ipsum dolor sit amet, consectetur adipiscing elit, sed do eiusmod tempor incididunt ut labore et dolore magna aliqua. Ut enim ad minim veniam, quis nostrud exercitation ullamco laboris nisi ut aliquip ex ea commodo consequat. Duis aute irure dolor in reprehenderit in voluptate velit esse cillum dolore eu fugiat nulla pariatur.</p>
      </div>
    </div>
    <div class="url-tab">www.velacredit.com</div>
  </article>

  <!-- Title loan payoff -->
  <article class="poster block p-title">
    <div class="bg bg-green" role="img" aria-label="Green banknote engraving pattern"></div>
    <div class="bg bg-red" role="img" aria-label="Red banknote engraving pattern"></div>
    <div class="frame"></div>
    <div class="title-head">
      <div class="q">¿ATASCADO EN UN PRÉSTAMO SOBRE EL TÍTULO?</div>
      <div class="kicker">PAGUEMOSLO HASTA</div>
      <div class="amount">$10,000</div>
      <div class="sub">( Stuck in a Title Loan? Let us pay it off up to $10,000 )</div>
    </div>
    <div class="panel"><div class="brand-name">Vela Credit</div><div class="bar">www.velacredit.com</div></div>
  </article>

  <!-- No credit check -->
  <article class="poster block p-credit">
    <div class="bg bg-green" role="img" aria-label="Green-tinted photo of dollar bills"></div>
    <div class="bg bg-red" role="img" aria-label="Red banknote engraving pattern"></div>
    <div class="frame"></div>
    <div class="no-box">NO</div>
    <div class="credit">CREDIT<br>CHECK</div>
    <p class="credit-note">Lorem ipsum dolor sit amet, consectetur adipiscing elit, sed do eiusmod tempor incididunt ut labore et dolore magna aliqua.</p>
    <div class="panel"><div class="brand-name">Vela Credit</div><div class="bar">www.velacredit.com</div></div>
  </article>
</body>
</html>
```